Our new beauty salon requires a price list brochure

Our beauty clinic is a medical grade skin care clinic. So our salon is very clinical and professional in appearance. I would like the colours to be similar to our logo design with some nice texture or abstract shapes thrown in.
Pricelist, contact details and logo is attached
I would prefer it to be a 3 fold brochure.

Target Market(s)

Females aged 30-50

Colors
85acd3
cedeed
c4c4c4
5c5c5c
000000
ffffff
eea3c7
f9d9e8
dbdbdb

Requirements
Must have
• easy to read

```html
<!DOCTYPE html>
<html lang="en">
<head>
<meta charset="utf-8">
<title>Alora Skin Studio – Price List Brochure</title>
<link rel="stylesheet" href="https://fonts.googleapis.com/css2?family=Montserrat:wght@400;500;600;800;900&display=swap">
<style>
:root{
  --backdrop:#38363c;
  --paper:#e1e6e4;
  --paper-dark:#ccd3d2;
  --slate:#4e5a68;
  --ink:#3c4550;
  --price:#56616d;
  --rule:#9aa4ad;
  --blue:#9fb4cf;
  --mint:#cde6d8;
  --lime:#e3e8b4;
  --blush:#f2c9b4;
  --skin:#e8c7b2;
  --white:#ffffff;
}
*{margin:0;padding:0;box-sizing:border-box}
html,body{width:942px;height:1200px;overflow:hidden}
body{background:var(--backdrop);font-family:"Montserrat",sans-serif;color:var(--ink);position:relative}
.sheet{position:absolute;left:156px;width:630px;height:487px;
  background:radial-gradient(ellipse at 30% 20%,#eef1ef 0%,var(--paper) 45%,var(--paper-dark) 100%)}
.sheet--outside{top:71px}
.sheet--inside{top:616px}
.panel{position:absolute;top:0;width:210px;height:487px;overflow:hidden}
.panel + .panel{border-left:1px solid #aab3ba}
.panel--1{left:0}.panel--2{left:210px}.panel--3{left:420px}
.art{position:absolute;left:0;top:0;width:210px;height:487px}
.abs{position:absolute}
.badge{position:absolute;border-radius:50%;background:var(--slate);color:var(--white);
  display:flex;align-items:center;justify-content:center;text-align:center;
  font-weight:900;text-transform:uppercase;line-height:.92;letter-spacing:-.2px}
.badge--md{width:74px;height:74px;font-size:12px}
.badge--lg{width:108px;height:108px;font-size:12.5px}
.badge--sm{font-size:8.5px}
.copy{position:absolute;font-size:7.6px;font-weight:500;line-height:9.6px}
.copy b{color:var(--price);font-weight:700}
.price-list{position:absolute;list-style:none;font-size:7.6px;font-weight:500}
.price-list li{display:flex;justify-content:space-between;align-items:flex-start;min-height:13.6px;line-height:9.6px;position:relative;padding-left:8px}
.price-list li::before{content:"";position:absolute;left:0;top:2.5px;border-left:3px solid var(--slate);border-top:2px solid transparent;border-bottom:2px solid transparent}
.price-list li.plain{padding-left:8px}
.price-list li.plain::before{display:none}
.price-list .price{color:var(--price);font-weight:700;text-align:right;white-space:nowrap}
.price-list .extra{display:flex;gap:12px}
.rule{position:absolute;height:1px;background:var(--rule)}
.contact-band{position:absolute;left:0;width:210px;top:418px;height:16px;background:var(--slate);color:var(--white);
  font-size:11px;font-weight:500;display:flex;align-items:center;justify-content:center;gap:5px}
.contact-line{position:absolute;left:0;width:210px;text-align:center;font-size:7.6px;font-weight:400;color:#5d6670;display:flex;justify-content:center;align-items:center;gap:4px}
.contact-line .dot{width:6px;height:6px;border-radius:50%;background:var(--slate);display:inline-block}
.address{position:absolute;left:0;width:210px;top:390px;text-align:center;font-size:7.6px;line-height:10px;color:#5d6670;text-transform:uppercase}
.brand-name{position:absolute;left:0;width:210px;top:222px;text-align:center;font-size:22px;font-weight:400;letter-spacing:3px;color:var(--slate);line-height:26px}
</style>
</head>
<body>

<!-- OUTSIDE SHEET -->
<section class="sheet sheet--outside">

  <!-- Panel 1: injectables & peels -->
  <div class="panel panel--1">
    <svg class="art" viewBox="0 0 210 487">
      <defs>
        <linearGradient id="skinA" x1="0" y1="0" x2="0" y2="1"><stop offset="0" stop-color="#e9cbb8"/><stop offset="1" stop-color="#dcb39c"/></linearGradient>
      </defs>
      <g role="img" aria-label="Portrait of a woman touching her forehead"><rect x="0" y="0" width="210" height="139" fill="url(#skinA)"/></g>
      <g role="img" aria-label="Smiling woman with smooth skin"><polygon points="60,243 134,243 97,303" fill="url(#skinA)"/></g>
      <circle cx="89" cy="294" r="5" fill="var(--slate)"/>
    </svg>

    <div class="copy" style="left:22px;top:147px;width:163px">
      <ul class="price-list" style="position:static;width:163px">
        <li><span>Wrinkle Relaxers per area</span><span class="price">$175</span></li>
      </ul>
      <div style="padding-left:8px;margin-top:-4px">(Crows, frown lines, forehead lines)</div>
      <div style="padding-left:8px;display:flex;justify-content:space-between"><span>or all 3 areas for</span><b>$450</b></div>
      <div style="padding-left:8px;margin-top:7px">$50 minor areas (Gummy smile,<br>brow lift, bunny lines)</div>
    </div>
    <div class="rule" style="left:28px;top:209px;width:158px"></div>

    <ul class="price-list" style="left:22px;top:218px;width:163px">
      <li><span>Dermal Fillers and<br>Lip Fillers</span><span class="price">$500<br>per ml</span></li>
    </ul>

    <div class="badge badge--md" style="left:127px;top:244px">Chemical<br>Peels</div>

    <ul class="price-list" style="left:22px;top:312px;width:163px">
      <li class="plain"><span>Verity Dr Peels 30min</span></li>
      <li><span>Lactic Acid Peels 20%/40%/60%</span><span class="price">$120</span></li>
      <li><span>Age Defining Peel</span><span class="price">$120</span></li>
      <li><span>Complete Pigment Peel</span><span class="price">$120</span></li>
      <li><span>Problem Skin Peel</span><span class="price">$120</span></li>
    </ul>

    <ul class="price-list" style="left:22px;top:394px;width:163px">
      <li class="plain"><span>Cellara Peels 30min</span></li>
      <li><span>Blueberry Peel</span><span class="price">$120</span></li>
      <li><span>Pomegranate Peel</span><span class="price">$120</span></li>
      <li><span>Benefit Peel</span><span class="price">$120</span></li>
      <li><span>Timeless Retinol Peel</span><span class="price">$250</span></li>
    </ul>
  </div>

  <!-- Panel 2: LED, laser, contact -->
  <div class="panel panel--2">
    <svg class="art" viewBox="0 0 210 487">
      <defs>
        <linearGradient id="ledGlow" x1="0" y1="0" x2="1" y2="1"><stop offset="0" stop-color="#3b1a63"/><stop offset=".5" stop-color="#b04ad8"/><stop offset="1" stop-color="#e08ff0"/></linearGradient>
        <linearGradient id="clinic" x1="0" y1="0" x2="1" y2="1"><stop offset="0" stop-color="#f1ece8"/><stop offset="1" stop-color="#d9b6a4"/></linearGradient>
      </defs>
      <g role="img" aria-label="LED light therapy treatment"><polygon points="120,106 204,106 162,178" fill="url(#ledGlow)"/></g>
      <circle cx="142" cy="164" r="6" fill="var(--slate)"/>
      <g role="img" aria-label="Laser facial being applied to a client"><polygon points="36,225 134,225 85,305" fill="url(#clinic)"/></g>
      <g role="img" aria-label="Client receiving a laser facial"><polygon points="8,365 106,365 57,282" fill="url(#clinic)"/></g>
      <polygon points="56,222 68,222 62,232" fill="var(--slate)"/>
      <circle cx="12" cy="304" r="5" fill="var(--slate)"/>
    </svg>

    <div class="badge badge--md" style="left:123px;top:21px">Lumora<br>LED</div>
    <ul class="price-list" style="left:15px;top:67px;width:110px">
      <li><span><b>$90</b> per treatment or</span></li>
      <li style="min-height:0"><span><b>$50</b> when added on<br>to any of our other<br>skin treatments.</span></li>
    </ul>
    <div class="rule" style="left:22px;top:106px;width:94px"></div>
    <div class="copy" style="left:23px;top:110px;width:100px">Dermaglide<br>Microneedling<br>(Collagen Induction<br>Therapy)</div>
    <ul class="price-list" style="left:15px;top:152px;width:110px">
      <li><span><b>$350</b> full face</span></li>
      <li><span><b>$450</b> face, neck and<br>décolletage</span></li>
    </ul>
    <div class="rule" style="left:22px;top:198px;width:160px"></div>

    <div class="badge badge--md" style="left:120px;top:244px">Novalux<br>Laser<br>Facial</div>
    <ul class="price-list" style="left:115px;top:326px;width:92px">
      <li><span><b>$350</b> full face</span></li>
      <li><span><b>$450</b> face, neck<br>and décolletage</span></li>
    </ul>

    <div class="address">4/28 Harbour Road, Cedar Bay<br>Western Australia</div>
    <div class="contact-band">
      <svg width="9" height="9" viewBox="0 0 24 24" aria-hidden="true"><path fill="#fff" d="M6.6 10.8c1.4 2.8 3.8 5.2 6.6 6.6l2.2-2.2c.3-.3.7-.4 1-.2 1.1.4 2.3.6 3.6.6.6 0 1 .4 1 1V20c0 .6-.4 1-1 1C10.6 21 3 13.4 3 4c0-.6.4-1 1-1h3.5c.6 0 1 .4 1 1 0 1.3.2 2.5.6 3.6.1.3 0 .7-.2 1z"/></svg>
      (08) 9000 4821
    </div>
    <div class="contact-line" style="top:441px"><span class="dot"></span>www.aloraskin.com.au</div>
    <div class="contact-line" style="top:455px"><span class="dot"></span>instagram alora_skin</div>
    <div class="contact-line" style="top:469px"><span class="dot"></span>facebook alora skin studio</div>
  </div>

  <!-- Panel 3: cover -->
  <div class="panel panel--3">
    <svg class="art" viewBox="0 0 210 487">
      <defs>
        <linearGradient id="skinB" x1="0" y1="0" x2="0" y2="1"><stop offset="0" stop-color="#f0d9cb"/><stop offset="1" stop-color="#e3bfa9"/></linearGradient>
        <linearGradient id="eyeTone" x1="0" y1="0" x2="0" y2="1"><stop offset="0" stop-color="#c99a80"/><stop offset="1" stop-color="#f3cdb8"/></linearGradient>
      </defs>
      <g role="img" aria-label="Portrait of a woman with clear skin"><polygon points="60,38 140,38 100,178" fill="url(#skinB)"/></g>
      <circle cx="36" cy="26" r="4" fill="var(--lime)"/>
      <polygon points="42,30 58,30 50,44" fill="var(--mint)"/>
      <circle cx="155" cy="85" r="16" fill="#c8cfd6"/>
      <circle cx="146" cy="120" r="3.5" fill="var(--blue)"/>
      <polygon points="160,128 168,116 176,128" fill="var(--blue)"/>
      <polygon points="72,252 84,246 84,260" fill="var(--slate)"/>
      <g role="img" aria-label="Close-up of an eye with brow make-up"><polygon points="32,326 194,326 113,485" fill="url(#eyeTone)"/></g>
      <circle cx="38" cy="372" r="16" fill="#c8cfd6"/>
      <polygon points="144,318 156,318 150,328" fill="var(--slate)"/>
      <circle cx="170" cy="314" r="3" fill="var(--slate)"/>
      <circle cx="56" cy="407" r="3.5" fill="var(--blue)"/>
      <polygon points="16,414 24,402 32,414" fill="var(--blue)"/>
      <circle cx="122" cy="452" r="7" fill="var(--mint)"/>
    </svg>
    <div class="brand-name">alora skin studio</div>
  </div>
</section>

<!-- INSIDE SHEET -->
<section class="sheet sheet--inside">

  <!-- Panel 1: IPL hair removal -->
  <div class="panel panel--1">
    <svg class="art" viewBox="0 0 210 487">
      <defs>
        <linearGradient id="skinC" x1="0" y1="0" x2="1" y2="1"><stop offset="0" stop-color="#dcae92"/><stop offset="1" stop-color="#f2dccd"/></linearGradient>
      </defs>
      <g role="img" aria-label="Woman with smooth underarm skin"><rect x="0" y="0" width="164" height="136" fill="url(#skinC)"/></g>
      <polygon points="60,134 72,134 66,144" fill="var(--slate)"/>
      <polygon points="142,180 154,180 148,190" fill="var(--slate)"/>
      <circle cx="34" cy="226" r="9" fill="#c8cfd6"/>
      <circle cx="48" cy="250" r="6" fill="var(--slate)"/>
      <g role="img" aria-label="Smooth legs after hair removal"><polygon points="140,278 202,278 171,348" fill="url(#skinC)"/></g>
      <circle cx="156" cy="333" r="5" fill="var(--slate)"/>
      <g role="img" aria-label="Smooth stomach and waist"><polygon points="14,456 92,456 53,394" fill="url(#skinC)"/></g>
      <polygon points="34,468 46,468 40,458" fill="var(--slate)"/>
      <circle cx="44" cy="402" r="5" fill="var(--slate)"/>
    </svg>

    <div class="badge badge--lg" style="left:102px;top:64px">IPL Hair<br>Removal</div>

    <ul class="price-list" style="left:14px;top:158px;width:92px">
      <li><span>Upper lip</span><span class="price">$50</span></li>
      <li><span>Chin</span><span class="price">$50</span></li>
      <li><span>Cheeks</span><span class="price">$75</span></li>
      <li><span>Whole face</span><span class="price">$350</span></li>
    </ul>
    <ul class="price-list" style="left:94px;top:226px;width:91px">
      <li><span>Bikini</span><span class="price">$90</span></li>
      <li><span>G String</span><span class="price">$120</span></li>
      <li><span>Brazilian</span><span class="price">$150</span></li>
    </ul>
    <div class="rule" style="left:14px;top:270px;width:114px"></div>
    <ul class="price-list" style="left:14px;top:281px;width:92px">
      <li><span>Underarms</span><span class="price">$90</span></li>
      <li><span>Half arm</span><span class="price">$180</span></li>
      <li><span>Full arm</span><span class="price">$250</span></li>
      <li><span>Half leg</span><span class="price">$290</span></li>
      <li><span>Thighs</span><span class="price">$290</span></li>
      <li><span>Full leg</span><span class="price">$490</span></li>
    </ul>
    <div class="rule" style="left:94px;top:370px;width:92px"></div>
    <ul class="price-list" style="left:94px;top:376px;width:91px">
      <li><span>Full back</span><span class="price">$350</span></li>
      <li><span>Shoulders</span><span class="price">$180</span></li>
      <li><span>Nipples</span><span class="price">$60</span></li>
      <li><span>Snail trail</span><span class="price">$50</span></li>
      <li><span>Stomach</span><span class="price">$250</span></li>
      <li><span>Chest</span><span class="price">$250</span></li>
      <li><span>Buttocks</span><span class="price">$200</span></li>
    </ul>
  </div>

  <!-- Panel 2: IPL photo rejuvenation & waxing -->
  <div class="panel panel--2">
    <svg class="art" viewBox="0 0 210 487">
      <defs>
        <linearGradient id="skinD" x1="0" y1="0" x2="0" y2="1"><stop offset="0" stop-color="#f4e2d6"/><stop offset="1" stop-color="#e2bca6"/></linearGradient>
      </defs>
      <g role="img" aria-label="Woman with radiant skin"><polygon points="74,180 152,180 113,108" fill="url(#skinD)"/></g>
      <polygon points="12,142 26,142 19,154" fill="var(--slate)"/>
      <circle cx="200" cy="146" r="6" fill="var(--slate)"/>
      <circle cx="186" cy="134" r="8" fill="#d6dce0"/>
      <g role="img" aria-label="Close-up of a groomed eyebrow and eyelashes"><polygon points="126,316 206,316 166,388" fill="url(#skinD)"/></g>
      <polygon points="134,316 146,316 140,326" fill="var(--slate)"/>
      <circle cx="154" cy="373" r="5" fill="var(--slate)"/>
      <circle cx="92" cy="456" r="6" fill="var(--slate)"/>
      <polygon points="94,470 94,478 88,474" fill="var(--slate)"/>
    </svg>

    <div class="badge badge--lg badge--sm" style="left:-2px;top:22px;width:88px;height:88px">IPL Photo<br>Rejuvenation</div>
    <ul class="price-list" style="left:90px;top:37px;width:95px">
      <li><span>Full face</span><span class="price">$350</span></li>
      <li><span>Neck</span><span class="price">$200</span></li>
      <li><span>Face, neck<br>ad décolletage</span><span class="price" style="padding-top:9px">$450</span></li>
      <li class="plain"><span>Spot Treatment</span><span class="price">$50</span></li>
    </ul>

    <div class="badge badge--md" style="left:135px;top:212px">Waxing</div>
    <ul class="price-list" style="left:24px;top:192px;width:86px">
      <li><span>Eyebrow</span><span class="price">$21</span></li>
      <li><span>Lip</span><span class="price">$15</span></li>
      <li><span>Chin</span><span class="price">$15</span></li>
      <li><span>Sides of face</span><span class="price">$20</span></li>
      <li><span>Underarm</span><span class="price">$20</span></li>
      <li><span>Forearm</span><span class="price">$25</span></li>
      <li><span>Full arm</span><span class="price">$35</span></li>
      <li><span>Lower leg</span><span class="price">$30</span></li>
      <li><span>Upper leg</span><span class="price">$30</span></li>
      <li><span>Full leg</span><span class="price">$50</span></li>
      <li><span>Inner thigh</span><span class="price">$10</span></li>
      <li><span>Snail trail</span><span class="price">$10</span></li>
      <li><span>Bikini</span><span class="price">$30</span></li>
      <li><span>G String</span><span class="price">$40</span></li>
      <li><span>Brazilian</span><span class="price">$50</span></li>
    </ul>
    <div class="rule" style="left:18px;top:404px;width:186px"></div>
    <ul class="price-list" style="left:24px;top:411px;width:162px">
      <li><span>Eyebrow wax and Lip wax</span><span class="price">$30</span></li>
      <li><span>Eyebrow, lip and chin wax</span><span class="price">$45</span></li>
    </ul>
  </div>

  <!-- Panel 3: mens waxing, tinting, facials -->
  <div class="panel panel--3">
    <svg class="art" viewBox="0 0 210 487">
      <defs>
        <linearGradient id="spa" x1="0" y1="0" x2="1" y2="1"><stop offset="0" stop-color="#b4826a"/><stop offset="1" stop-color="#f1e6df"/></linearGradient>
      </defs>
      <g role="img" aria-label="Client relaxing with a facial mask"><polygon points="52,250 156,250 104,344" fill="url(#spa)"/></g>
      <polygon points="116,250 130,250 123,262" fill="var(--slate)"/>
      <circle cx="58" cy="290" r="14" fill="#c8cfd6"/>
      <polygon points="46,336 52,327 58,336" fill="#8e99a3"/>
      <circle cx="72" cy="330" r="3" fill="#8e99a3"/>
      <circle cx="162" cy="333" r="8" fill="var(--slate)"/>
    </svg>

    <ul class="price-list" style="left:25px;top:26px;width:87px">
      <li><span>Mono brow</span><span class="price">$5</span></li>
      <li><span>Eyebrow</span><span class="price">$21</span></li>
      <li><span>Neck</span><span class="price">$20</span></li>
      <li><span>Full back</span><span class="price">$45</span></li>
      <li><span>Chest and<br>Abdomen</span><span class="price" style="padding-top:9px">$45</span></li>
    </ul>
    <div class="badge badge--md" style="left:121px;top:25px">Mens<br>Waxing</div>
    <div class="rule" style="left:16px;top:113px;width:172px"></div>

    <div class="badge badge--md" style="left:9px;top:134px">Tinting</div>
    <ul class="price-list" style="left:89px;top:130px;width:87px">
      <li><span>Eyelash Tint</span><span class="price">$25</span></li>
      <li><span>Lash Lift &amp; Tint</span><span class="price">$80</span></li>
    </ul>
    <div class="rule" style="left:92px;top:162px;width:94px"></div>
    <ul class="price-list" style="left:89px;top:171px;width:87px">
      <li style="min-height:24px"><span>Henna eyebrows<br>and wax</span><span class="price" style="padding-top:9px">$80</span></li>
      <li><span>Eyelash Tint<br>and brow wax</span><span class="price" style="padding-top:9px">$40</span></li>
    </ul>

    <ul class="price-list" style="left:19px;top:362px;width:172px">
      <li><span>Alora Mini Facial</span><span class="extra"><span class="price">$80</span><span>40min</span></span></li>
    </ul>
    <div class="rule" style="left:19px;top:380px;width:168px"></div>
    <ul class="price-list" style="left:19px;top:389px;width:172px">
      <li><span>Alora Deluxe Facial</span><span class="extra"><span class="price">$110</span><span>1 hour</span></span></li>
    </ul>
    <div class="rule" style="left:19px;top:408px;width:168px"></div>
    <ul class="price-list" style="left:19px;top:417px;width:116px">
      <li><span>Microdermabrasion</span><span class="price">$125</span></li>
    </ul>
    <div class="rule" style="left:19px;top:435px;width:168px"></div>
    <ul class="price-list" style="left:19px;top:444px;width:116px">
      <li><span>Mini Micro</span><span class="price">$80</span></li>
    </ul>
  </div>
</section>

</body>
</html>
```